Quellmoor

We have already had a logo designed. Attached is the logo.
We are now wanting to design a label that will wrap around a plastic bottle which contains 1 litre of fluid. The size of the label is 15cm high by 28 cm wide.
The bottle for which the label will be used is a natural wellbeing supplement in a class of its own. It is a liquid tonic/complementary medicine - not a drink you guzzle down like zestorin.
The label needs to look natural and healthy and include the logo attached.
This is a premium bottle which will cost more than $50 AUD per bottle. The label needs to be classy as you would expect to find on an expensive bottle of wine.
The label needs to be able to sell the bottle and it needs to convince that what is inside the bottle is worth what it will cost.
The product does not have fruit in it and is not a water drink. One of the ingredients is an extract from the French Maritime Pine Bark.
We do not want the label to be to busy.
The product is to market in China, United States and Australia.
We will have to typeset certain wording onto the label - Ingredients, company details, bottle code etc which will be on the back of the bottle.
Updates

We have uploaded a picture of the plastic bottle that the label will be used on. The dimensions of the label have been included in the project brief.

Regards

Reason: We realise that the time period allowed to create a label may have been to short for some designers. Thanks

Reason: Just waiting on final designs to be submitted. This will be the last extension. Regards

Target Market(s)

Generally adults aged 35 to 65.

Industry/Entity Type

Plastic

Requirements
Must have
• Most of this information has been outlined above.

```html
<!DOCTYPE html>
<html lang="en">
<head>
<meta charset="utf-8">
<title>Quellmoor – Nature Inside label</title>
<link rel="stylesheet" href="https://fonts.googleapis.com/css2?family=Ubuntu:wght@400&family=Encode+Sans+Condensed:wght@300&display=swap">
<style>
  :root {
    --ink: #1b1d1e;
    --paper: #ffffff;
    --mint: #a9dcbf;
    --mint-pale: #d7efe1;
    --bar: #1a1c1d;
    --bar-tint: #25473a;
    --forest-top: #c7d4c6;
    --forest-mid: #6e5a3c;
    --forest-low: #6f9a3a;
  }
  * { margin: 0; padding: 0; box-sizing: border-box; }
  html, body { width: 1200px; height: 1000px; overflow: hidden; background: var(--paper); }
  .canvas { position: relative; width: 1200px; height: 1000px; background: var(--paper); }

  .label { position: absolute; left: 0; top: 176px; width: 1200px; height: 642px; background: var(--paper); overflow: hidden; }

  .pattern { position: absolute; top: 0; height: 642px;
    background: linear-gradient(135deg, var(--mint-pale), var(--mint) 50%, var(--mint-pale)); }
  .pattern--left { left: 0; width: 345px; }
  .pattern--right { left: 855px; width: 345px; }

  .bar { position: absolute; background: linear-gradient(180deg, var(--bar), var(--bar-tint) 50%, var(--bar)); }
  .bar--left { left: 0; top: 117px; width: 108px; height: 409px; }
  .bar--right { left: 934px; top: 0; width: 157px; height: 642px; }

  .rule-v { position: absolute; top: 54px; width: 1px; height: 535px; background: var(--ink); }

  .side-line { position: absolute; top: 321px; width: 300px; margin-left: -150px;
    font-family: "Ubuntu", sans-serif; font-size: 12px; color: var(--ink);
    text-align: center; transform: translateY(-50%) rotate(-90deg); white-space: nowrap; }

  .forest { position: absolute; left: 502px; top: 54px; width: 193px; height: 195px; }

  .brand-mark { position: absolute; right: 400px; top: 72px; display: flex; align-items: center; gap: 6px;
    font-family: "Ubuntu", sans-serif; font-size: 14px; color: var(--ink); }
  .brand-mark .dot { width: 10px; height: 10px; border-radius: 50%; background: var(--ink); }

  .product-name { position: absolute; left: 400px; width: 400px; top: 276px; text-align: center;
    font-family: "Ubuntu", sans-serif; font-weight: 400; font-size: 46px; color: var(--ink); letter-spacing: 0.5px; }

  .rule-h { position: absolute; left: 462px; width: 275px; height: 2px; background: var(--ink); }
  .rule-h--top { top: 364px; }
  .rule-h--bottom { top: 587px; }

  .tagline { position: absolute; left: 400px; width: 400px; top: 388px; text-align: center;
    font-family: "Encode Sans Condensed", sans-serif; font-weight: 300; font-size: 80px; line-height: 94px;
    color: var(--ink); letter-spacing: 1px; }
</style>
</head>
<body>
<div class="canvas">
  <section class="label">
    <div class="pattern pattern--left" role="img" aria-label="Mint green chevron zigzag pattern"></div>
    <div class="bar bar--left"></div>

    <div class="pattern pattern--right" role="img" aria-label="Mint green chevron zigzag pattern"></div>
    <div class="bar bar--right"></div>

    <div class="rule-v" style="left:344px"></div>
    <div class="rule-v" style="left:383px"></div>
    <div class="rule-v" style="left:816px"></div>
    <div class="rule-v" style="left:855px"></div>

    <p class="side-line" style="left:364px">Strength of nature for your health</p>
    <p class="side-line" style="left:836px">Strength of nature for your health</p>

    <svg class="forest" viewBox="0 0 193 195" role="img" aria-label="Pine forest photograph in a triangle">
      <defs>
        <linearGradient id="forestTone" x1="0" y1="0" x2="0" y2="1">
          <stop offset="0" stop-color="var(--forest-top)"/>
          <stop offset="0.3" stop-color="var(--forest-mid)"/>
          <stop offset="0.62" stop-color="var(--forest-mid)"/>
          <stop offset="0.75" stop-color="var(--forest-low)"/>
          <stop offset="1" stop-color="var(--forest-low)"/>
        </linearGradient>
      </defs>
      <polygon points="96.5,0 193,195 0,195" fill="url(#forestTone)"/>
    </svg>

    <div class="brand-mark"><span class="dot"></span>Quellmoor</div>

    <h1 class="product-name">Quellmoor</h1>
    <div class="rule-h rule-h--top"></div>
    <p class="tagline">NATURE<br>INSIDE</p>
    <div class="rule-h rule-h--bottom"></div>
  </section>
</div>
</body>
</html>
```